Personal Business Card Design Project

I am looking for a business card to be able to hand to both Chinese and Australian businessman.
I am a self employed consultant and just need my name, phone number and email address on the card. No Business Name and No Website.
I want it to look like an exclusive prestigious card.
I would like the background to be be a glossy red and the writing to be gold. (This applies to both sides of the card).
It must have English on one side and Chinese (Mandarin) on the reverse.
Details you will require
Name : Wade Emmerson
Phone : + 61 493 207 158
Email : wadeyemmerson@brightpost.example
Thank you everybody for your designs.
Industry/Entity Type
Business

```html
<!DOCTYPE html>
<html lang="zh-Hans">
<head>
<meta charset="utf-8">
<title>Wade Emmerson – 名片</title>
<link rel="stylesheet" href="https://fonts.googleapis.com/css2?family=Jost:wght@300&family=Noto+Sans+SC:wght@300&display=swap">
<style>
  :root {
    --card-red: #c20016;
    --gold: #e0b84a;
    --latin: "Jost", sans-serif;
    --hanzi: "Noto Sans SC", sans-serif;
  }
  html, body {
    margin: 0;
    padding: 0;
    width: 1200px;
    height: 734px;
    overflow: hidden;
    background: var(--card-red);
  }
  .card {
    position: relative;
    width: 1200px;
    height: 734px;
    background: var(--card-red);
    color: var(--gold);
    font-family: var(--latin);
    font-weight: 300;
  }
  .card-name {
    position: absolute;
    left: 0;
    right: 0;
    top: 205px;
    margin: 0;
    text-align: center;
    font-family: var(--latin);
    font-weight: 300;
    font-size: 58px;
    letter-spacing: 2px;
    line-height: 1;
    transform: translateX(-13px);
  }
  .contact-list {
    position: absolute;
    left: 175px;
    top: 606px;
    margin: 0;
    padding: 0;
    list-style: none;
    font-size: 45px;
    line-height: 56px;
    white-space: nowrap;
  }
  .contact-label {
    font-family: var(--hanzi);
    font-weight: 300;
  }
  .contact-value {
    font-family: var(--latin);
    font-weight: 300;
  }
</style>
</head>
<body>
  <main class="card">
    <h1 class="card-name">Wade Emmerson</h1>
    <ul class="contact-list">
      <li class="contact-item"><span class="contact-label">电话:</span> <span class="contact-value">+ 61 493 207 158</span></li>
      <li class="contact-item"><span class="contact-label">电子邮件:</span>&nbsp; <span class="contact-value">wadeyemmerson@brightpost.example</span></li>
    </ul>
  </main>
</body>
</html>
```